Demo Screens Needed for Recruiting with AI App

We are in the process of raising money for our startup called KelvoraLink. We need demos to show investors what we're trying to do with images. We really love the simplicity and modern look of the Pivlo App and want something similar. We will have the "swipe" functionality similar to Flarvi as well. The sample images I've attached are only for caregivers but long term this will be for all industries. There will also be a rewards page for loyalty membership. The current landing page is www.kelvoralink-demo.com. That will show you the color scheme and logo.

```html
<!DOCTYPE html>
<html lang="en">
<head>
<meta charset="utf-8">
<title>KelvoraLink – App Screens</title>
<link href="https://fonts.googleapis.com/css2?family=Open+Sans:wght@300;400;600;700&display=swap" rel="stylesheet">
<style>
:root{
  --stage:#dcdde0;
  --ink:#1c1c1f;
  --muted:#55585e;
  --brand-blue:#1b6a9a;
  --deep-navy:#0d0f2b;
  --deep-purple:#2a1552;
  --violet:#4a2a9c;
  --chip:#eceef1;
  --panel:#f1f2f4;
  --star:#f0b400;
  --white:#ffffff;
}
*{box-sizing:border-box;margin:0;padding:0}
html,body{width:1200px;height:753px;overflow:hidden;background:var(--stage);font-family:"Open Sans",sans-serif;color:var(--ink)}
.stage{position:relative;width:1200px;height:753px}
.screen{position:absolute;top:36px;width:340px;height:680px;border-radius:38px;overflow:hidden;background:var(--white)}
.screen--welcome{left:40px;background:linear-gradient(180deg,#171340 0%,var(--deep-purple) 22%,var(--deep-navy) 55%,#0f2a33 85%,#0c1c24 100%)}
.screen--browse{left:430px}
.screen--profile{left:820px}
.status{position:absolute;top:20px;left:28px;right:26px;display:flex;justify-content:space-between;align-items:center;font-size:13px;color:#777}
.screen--welcome .status{color:var(--white);font-weight:600}
.status svg{display:block}
.wordmark{font-weight:300;letter-spacing:3px;text-transform:uppercase}
.welcome-art{position:absolute;inset:0;background:radial-gradient(ellipse at 50% 25%,rgba(90,70,170,.35),transparent 60%),radial-gradient(ellipse at 50% 85%,rgba(40,110,120,.35),transparent 60%)}
.welcome-logo{position:absolute;top:124px;width:100%;text-align:center;color:var(--white);font-size:29px;letter-spacing:4px}
.tagline{position:absolute;top:402px;width:100%;text-align:center;color:var(--white);font-weight:700;font-size:18.5px;line-height:28px}
.btn{position:absolute;left:58px;width:240px;height:44px;border-radius:22px;display:flex;align-items:center;justify-content:center;font-size:13.5px}
.btn--primary{top:496px;background:var(--violet);color:var(--white)}
.btn--secondary{top:545px;background:var(--white);color:var(--violet)}
.home-bar{position:absolute;bottom:40px;left:50%;transform:translateX(-50%);width:130px;height:4px;border-radius:2px;background:var(--ink)}
.screen--welcome .home-bar{background:var(--white)}
.app-logo{position:absolute;top:62px;left:29px;font-size:17px;color:var(--ink);letter-spacing:2.5px}
.page-title{position:absolute;top:93px;left:32px;color:var(--brand-blue);font-weight:700;font-size:14px}
.filters{position:absolute;top:122px;left:28px;right:14px;display:flex;gap:5px;align-items:center}
.chip{height:22px;padding:0 8px;border-radius:11px;background:var(--chip);font-size:8px;color:#444;display:flex;align-items:center;gap:4px;white-space:nowrap}
.search{margin-left:6px}
.section-label{position:absolute;top:167px;left:29px;font-size:12.5px;font-weight:400}
.sitter-list{position:absolute;top:190px;left:29px;right:30px}
.sitter{position:relative;display:flex;gap:10px;height:93px}
.avatar{flex:0 0 68px;height:76px;border-radius:3px}
.sitter-body{flex:1;position:relative;padding-top:5px}
.sitter-name{font-size:12.5px;line-height:17px}
.sitter-city{font-size:9.5px;line-height:13px;margin-top:2px}
.sitter-rate{position:absolute;top:0;right:0;text-align:right;font-size:9.5px}
.stars{color:var(--star);font-size:12px;letter-spacing:-1px}
.stars small{color:#666;font-size:8px;margin-left:4px;letter-spacing:0}
.sitter-note{font-size:7.6px;line-height:12.5px;color:#444;margin-top:8px}
.sitter--last{height:56px}
.sitter--last .avatar{height:44px}
.sitter--last .sitter-note{margin-top:4px}
.profile-name{position:absolute;top:92px;left:32px;font-size:12.5px;font-weight:400}
.profile-facts{position:absolute;top:115px;left:28px;right:30px;height:36px;background:var(--panel);display:flex;align-items:center;justify-content:space-between;padding:0 8px;font-size:9.5px}
.fact{display:flex;align-items:center;gap:5px;line-height:12px}
.traits{position:absolute;top:168px;left:26px;right:20px;list-style:none}
.trait{display:flex;align-items:center;gap:16px;font-size:10.8px;height:37px}
.trait svg{flex:0 0 22px}
.hero-photo{position:absolute;left:0;right:0;bottom:0;height:236px;border-radius:26px 26px 0 0;background:linear-gradient(180deg,#8ea95d 0%,#5f8a3c 45%,#3d5d2a 100%)}
</style>
</head>
<body>
<main class="stage">

  <section class="screen screen--welcome" aria-label="Welcome screen">
    <div class="welcome-art" role="img" aria-label="Abstract dark background with faint digital pattern"></div>
    <div class="status"><span>7:43</span>
      <svg width="52" height="12" viewBox="0 0 52 12" fill="#fff"><rect x="0" y="8" width="3" height="4"/><rect x="4" y="6" width="3" height="6"/><rect x="8" y="3" width="3" height="9"/><rect x="12" y="0" width="3" height="12"/><path d="M19 4a9 9 0 0 1 12 0l-1.5 1.5a7 7 0 0 0-9 0zM22 7a5 5 0 0 1 6 0l-3 3z"/><rect x="34" y="2" width="16" height="8" rx="2"/></svg>
    </div>
    <div class="welcome-logo wordmark">KelvoraLink</div>
    <p class="tagline">Unlocking the Power<br>Of Meaningful Connections</p>
    <div class="btn btn--primary">Create Account</div>
    <div class="btn btn--secondary">Sign in</div>
    <div class="home-bar"></div>
  </section>

  <section class="screen screen--browse" aria-label="Caregiver list">
    <div class="status"><span>7:43</span>
      <svg width="52" height="12" viewBox="0 0 52 12" fill="#888"><rect x="0" y="8" width="3" height="4"/><rect x="4" y="6" width="3" height="6"/><rect x="8" y="3" width="3" height="9"/><rect x="12" y="0" width="3" height="12"/><path d="M19 4a9 9 0 0 1 12 0l-1.5 1.5a7 7 0 0 0-9 0zM22 7a5 5 0 0 1 6 0l-3 3z"/><rect x="34" y="2" width="16" height="8" rx="2"/></svg>
    </div>
    <div class="app-logo wordmark">KelvoraLink</div>
    <h1 class="page-title">Find Yout Tribe</h1>
    <div class="filters">
      <span class="chip"><svg width="7" height="10" viewBox="0 0 7 10"><path d="M3.5 0a3.5 3.5 0 0 0-3.5 3.5C0 6 3.5 10 3.5 10S7 6 7 3.5A3.5 3.5 0 0 0 3.5 0z" fill="#555"/></svg>Palo Alto -15mi</span>
      <span class="chip"><svg width="9" height="9" viewBox="0 0 9 9"><rect x=".5" y="1.5" width="8" height="7" fill="none" stroke="#555"/><path d="M.5 3.5h8" stroke="#555"/></svg>Date</span>
      <span class="chip"><svg width="9" height="9" viewBox="0 0 9 9"><circle cx="4.5" cy="4.5" r="4" fill="none" stroke="#555"/><path d="M4.5 2v2.5l2 1" stroke="#555" fill="none"/></svg>$25/hr</span>
      <span class="chip">More <svg width="7" height="5" viewBox="0 0 7 5"><path d="M.5.5l3 3 3-3" stroke="#555" fill="none"/></svg></span>
      <svg class="search" width="15" height="15" viewBox="0 0 15 15"><circle cx="6" cy="6" r="5" fill="none" stroke="#333" stroke-width="1.3"/><path d="M10 10l4 4" stroke="#333" stroke-width="1.3"/></svg>
    </div>
    <h2 class="section-label">Message</h2>
    <div class="sitter-list">
      <article class="sitter">
        <div class="avatar" role="img" aria-label="Portrait photo of Jules M." style="background:linear-gradient(160deg,#6f7a5e,#3b3a36)"></div>
        <div class="sitter-body">
          <div class="sitter-name">Jules M.</div><div class="sitter-city">Palo Alto, CA</div>
          <div class="sitter-rate">From $25 per/hr<div class="stars">★★★★★<small>(7)</small></div></div>
          <p class="sitter-note">One thing I prioritize in childcare is Creating a fun and engaging atmosphere where children can explore, play, and express themselves creatively</p>
        </div>
      </article>
      <article class="sitter">
        <div class="avatar" role="img" aria-label="Portrait photo of Charlize J." style="background:linear-gradient(160deg,#a08067,#4a3328)"></div>
        <div class="sitter-body">
          <div class="sitter-name">Charlize J.</div><div class="sitter-city">Los Altos, CA</div>
          <div class="sitter-rate">From $25 per/hr<div class="stars">★★★★★<small>(5)</small></div></div>
          <p class="sitter-note">An ideal playdate to me is active play, exploration and creativity, such as running around the park with a scavenger hunt, then a book to wind down</p>
        </div>
      </article>
      <article class="sitter">
        <div class="avatar" role="img" aria-label="Portrait photo of Nicola L." style="background:linear-gradient(160deg,#8a6a4e,#3a2a20)"></div>
        <div class="sitter-body">
          <div class="sitter-name">Nicola L.</div><div class="sitter-city">Menlo Park, CA</div>
          <div class="sitter-rate">From $20 per/hr<div class="stars">★★★★★<small>(9)</small></div></div>
          <p class="sitter-note">One thing I prioritize in childcare is a safe environment both physically and mentally</p>
        </div>
      </article>
      <article class="sitter">
        <div class="avatar" role="img" aria-label="Portrait photo of Ana V." style="background:linear-gradient(160deg,#9a7a66,#2e2622)"></div>
        <div class="sitter-body">
          <div class="sitter-name">Ana V.</div><div class="sitter-city">Palo Alto, CA</div>
          <div class="sitter-rate">From $25 per/hr<div class="stars">★★★★★<small>(2)</small></div></div>
          <p class="sitter-note">Outdoor play is important because it promotes physical activity that helps with gross motor skills all while soaking up the vitamin d and fresh air</p>
        </div>
      </article>
      <article class="sitter sitter--last">
        <div class="avatar" role="img" aria-label="Portrait photo of Emily M." style="background:linear-gradient(160deg,#6a4a3a,#1e1612)"></div>
        <div class="sitter-body">
          <div class="sitter-name">Emily M.</div><div class="sitter-city">Redwood City CA</div>
          <div class="sitter-rate">From $24 per/hr<div class="stars">★★★★★<small>(2)</small></div></div>
          <p class="sitter-note">I am comfortable with pets and can handle a bunch ....</p>
        </div>
      </article>
    </div>
    <div class="home-bar"></div>
  </section>

  <section class="screen screen--profile" aria-label="Caregiver profile">
    <div class="status"><span>7:43</span>
      <svg width="52" height="12" viewBox="0 0 52 12" fill="#888"><rect x="0" y="8" width="3" height="4"/><rect x="4" y="6" width="3" height="6"/><rect x="8" y="3" width="3" height="9"/><rect x="12" y="0" width="3" height="12"/><path d="M19 4a9 9 0 0 1 12 0l-1.5 1.5a7 7 0 0 0-9 0zM22 7a5 5 0 0 1 6 0l-3 3z"/><rect x="34" y="2" width="16" height="8" rx="2"/></svg>
    </div>
    <div class="app-logo wordmark">KelvoraLink</div>
    <h1 class="profile-name">Jules</h1>
    <div class="profile-facts">
      <span class="fact"><svg width="18" height="16" viewBox="0 0 18 16" fill="none" stroke="#333"><rect x="2" y="6" width="14" height="9"/><circle cx="5" cy="3" r="2"/><circle cx="13" cy="3" r="2"/></svg><span>10 Yrs<br>Experience</span></span>
      <span class="fact"><svg width="12" height="13" viewBox="0 0 12 13" fill="none" stroke="#333"><circle cx="6" cy="4" r="3"/><path d="M1 12.5a5 5 0 0 1 10 0z"/></svg>Female</span>
      <span class="fact"><svg width="13" height="13" viewBox="0 0 13 13" fill="none" stroke="#333"><circle cx="6.5" cy="6.5" r="5.8"/><path d="M6.5 3v3.5l2.5 1.5"/></svg>$25-$35/hr</span>
      <span class="fact"><svg width="14" height="13" viewBox="0 0 14 13" fill="none" stroke="#333"><path d="M7 .8l1.9 3.9 4.2.6-3 3 .7 4.2L7 10.5 3.2 12.5l.7-4.2-3-3 4.2-.6z"/></svg>5</span>
    </div>
    <ul class="traits">
      <li class="trait"><svg width="22" height="22" viewBox="0 0 22 22" fill="none" stroke="#333" stroke-width="1.2"><path d="M2 11L11 3l9 8M5 9v10h12V9"/><path d="M9 19v-5h4v5"/></svg>Palo,Alto, California</li>
      <li class="trait"><svg width="22" height="22" viewBox="0 0 22 22" fill="none" stroke="#333" stroke-width="1.2"><rect x="2" y="3" width="11" height="13"/><rect x="9" y="7" width="11" height="13" fill="#fff"/><path d="M5 12l2.5-6 2.5 6M12 11h6M15 11c0 4-2 6-3 6M15 11c0 3 2 5 3 6"/></svg>English,Spanish, Mandarin</li>
      <li class="trait"><svg width="22" height="22" viewBox="0 0 22 22" fill="none" stroke="#333" stroke-width="1.2"><rect x="2" y="4" width="18" height="13"/><path d="M5 8h12M5 11h8M5 14h6"/><circle cx="16" cy="15" r="2.5"/></svg>Bachelor's Degree</li>
      <li class="trait"><svg width="22" height="22" viewBox="0 0 22 22" fill="none" stroke="#333" stroke-width="1.2"><circle cx="11" cy="6" r="4"/><path d="M5 21v-6a6 6 0 0 1 12 0v6zM8 16h6"/></svg>Age Groups: 0-11mo,1-3 yrs, 4-5 yrs</li>
      <li class="trait"><svg width="22" height="22" viewBox="0 0 22 22" fill="none" stroke="#333" stroke-width="1.2"><rect x="2" y="6" width="18" height="13"/><path d="M8 6V3h6v3M2 11h18M11 9v4"/></svg>CPR Trained ,Special Needs Care</li>
      <li class="trait"><svg width="22" height="22" viewBox="0 0 22 22" fill="none" stroke="#333" stroke-width="1.2"><circle cx="11" cy="11" r="9"/><circle cx="11" cy="11" r="7"/><path d="M11 6v5l3 2"/></svg>Full-time,open to part time</li>
      <li class="trait"><svg width="22" height="22" viewBox="0 0 22 22" fill="none" stroke="#333" stroke-width="1.2"><path d="M11 2v18M2 11h18"/></svg>Comfortable with pets,Meal prep</li>
    </ul>
    <div class="hero-photo" role="img" aria-label="Photo of Jules smiling outdoors in a sunny park"></div>
    <div class="home-bar" style="background:var(--white);bottom:26px"></div>
  </section>

</main>
</body>
</html>
```